Recruitment Site Design

We need a design for the login page, about page, and inner pages of a recruitment site for an oil and gas company. Design should be modern, sleek, professional and colors can be blue, green, white, orange or any other recommended colors.

Please also take into consideration that once the users login, they will need to access a form to fill in their information.

** UPDATE: Kindly provide a design for the inner information page consistent with the outer design. Attached is a picture of the basic structure. ***
Updates

Please provide a design for inner pages as shown in the design brief consistent with the registration page provided. 

Reason: We're extending it to get more inside pages.

Target Market(s)

Professionals looking for a career in the oil and gas industry in the Middle East.

Industry/Entity Type

Oil And Gas

Requirements
Must have
• Sleek design

```html
<!DOCTYPE html>
<html lang="en">
<head>
<meta charset="utf-8">
<title>Vantra – Oil &amp; Gas Careers</title>
<link href="https://fonts.googleapis.com/css2?family=PT+Sans:ital,wght@0,400;0,700;1,400;1,700&family=Open+Sans:wght@400;600&display=swap" rel="stylesheet">
<style>
:root{
  --dark:#2a1f10;
  --red:#d42e05;
  --red-deep:#b82503;
  --text:#3a3a3a;
  --muted:#999;
  --line:#dcdcdc;
  --white:#fff;
  --btn:#1f1f1f;
}
*{margin:0;padding:0;box-sizing:border-box}
html,body{width:1056px;height:1200px;overflow:hidden;background:var(--white)}
body{position:relative;font-family:"PT Sans",sans-serif;color:var(--text)}
.abs{position:absolute}
.header-band{left:0;top:0;width:1056px;height:322px;background:var(--dark)}
.brand{left:110px;top:22px;font-family:"PT Sans",sans-serif;font-weight:700;font-size:46px;color:var(--red);letter-spacing:2px}
.main-nav{top:57px;left:0;font-family:Georgia,serif;font-style:italic;font-weight:700;font-size:14.5px}
.main-nav a{position:absolute;color:var(--red);text-decoration:none;white-space:nowrap}
.main-nav a.current{color:var(--white)}
.hero{left:88px;top:102px;width:880px;height:339px;background:var(--red)}
.hero-photo{left:94px;top:109px;width:582px;height:325px;background:linear-gradient(180deg,#f0b43a 0%,#f5c24a 40%,#e39a1c 70%,#5a3a12 100%)}
.slide-dots span{position:absolute;top:414px;width:9px;height:9px;background:#111}
.slide-dots span.on{background:var(--white)}
.hero-title{left:686px;top:116px;font-family:Georgia,serif;font-style:italic;font-weight:700;font-size:30px;color:var(--white)}
.hero-sub{left:686px;color:var(--white);font-size:17px}
.hero-note{left:686px;top:209px;width:275px;font-size:10px;line-height:12.5px;color:var(--white);font-weight:700}
.form-label{font-family:"Open Sans",sans-serif;font-size:15px;color:var(--white);text-align:right;width:110px;left:641px}
.field{left:760px;width:153px;height:23px;background:var(--white);border-radius:7px}
.search-btn{left:762px;top:372px;width:128px;height:31px;border-radius:6px;background:linear-gradient(#3a3a3a,#0d0d0d);color:var(--white);font-family:"Open Sans",sans-serif;font-size:16px;text-align:center;line-height:31px;box-shadow:0 2px 3px rgba(0,0,0,.4)}
.slide-tab{left:942px;top:248px;width:30px;height:49px}
.hero-shadow{left:200px;top:441px;width:700px;height:12px;background:radial-gradient(ellipse at top,rgba(0,0,0,.35),transparent 70%)}
h2{font-weight:700;color:var(--red);font-size:21px}
.welcome-title{left:94px;top:450px}
.welcome-photo{left:99px;top:495px;width:212px;height:205px;background:linear-gradient(180deg,#8ba9c4 0%,#f0b45c 45%,#f29a2c 60%,#3a2a20 100%)}
.photo-shadow{left:105px;top:700px;width:200px;height:10px;background:radial-gradient(ellipse at top,rgba(0,0,0,.35),transparent 70%)}
.body-copy{font-size:11.4px;line-height:21.1px;color:#444}
.body-copy a{color:var(--red);font-style:italic;font-weight:700}
.copy-side{left:326px;top:488px;width:310px;text-align:left}
.copy-full{left:95px;top:717px;width:545px}
.box{border:1px solid var(--line);background:var(--white)}
.careers{left:652px;top:457px;width:267px;height:355px}
.careers h2{position:absolute;left:23px;top:3px}
.careers ul{position:absolute;left:24px;top:45px;list-style:none;font-style:italic;font-size:11.5px;color:#222}
.careers li{height:31.7px;padding-left:15px;position:relative}
.careers li::before{content:"";position:absolute;left:0;top:4px;border-left:5px solid #222;border-top:3.5px solid transparent;border-bottom:3.5px solid transparent}
.jobs{left:90px;top:822px;width:266px;height:289px}
.testimonial{left:370px;top:822px;width:266px;height:289px}
.panel-title{position:absolute;left:10px;top:6px}
.job-item{position:absolute;left:11px;width:245px;font-size:12.5px;line-height:15px;color:#222}
.job-date,.job-head{color:var(--red);font-size:12.5px}
.job-head{margin:3px 0 4px}
.read-more{display:block;margin-top:10px;color:var(--red);font-style:italic;text-decoration:underline;font-size:12px}
.read-more::before{content:"";display:inline-block;width:13px;height:7px;margin-right:5px;background:radial-gradient(circle at 3px 3.5px,#f39a1f 3px,transparent 3.3px),radial-gradient(circle at 10px 3.5px,#f39a1f 3px,transparent 3.3px)}
.quote-mark{position:absolute;font-family:Georgia,serif;font-size:34px;color:#c8c8c8;font-weight:700;font-style:italic}
.quote-text{position:absolute;left:17px;top:66px;width:242px;text-align:justify;font-size:12px;line-height:17.6px;color:#444}
.quote-text a{color:var(--red);font-style:italic;font-weight:700}
.quote-by{position:absolute;right:20px;top:236px;color:var(--red);font-style:italic;font-size:20px}
.call{left:652px;top:820px;width:267px;height:179px;overflow:hidden}
.call-photo{left:0;top:0;width:140px;height:179px;background:linear-gradient(135deg,#e8e2dc,#c9a48a 55%,#f3f0ec)}
.call-title{position:absolute;left:140px;top:55px;width:120px;text-align:center;color:var(--red);font-style:italic;font-size:22px;font-family:"Open Sans",sans-serif}
.call-phone{position:absolute;left:148px;top:86px;color:var(--red);font-size:17px;font-family:"Open Sans",sans-serif}
.call-btn{position:absolute;left:142px;top:131px;width:110px;height:27px;border-radius:8px;background:linear-gradient(#fff,#dcdcdc);box-shadow:0 1px 3px rgba(0,0,0,.35);font-family:"Open Sans",sans-serif;font-size:11.5px;line-height:27px;padding-left:11px;color:#222}
.call-btn svg{position:absolute;right:8px;top:4px}
.newsletter{left:652px;top:1009px;width:267px;height:102px}
.newsletter h2{position:absolute;left:5px;top:4px}
.mail-field{position:absolute;left:12px;top:41px;width:232px;height:27px;border:1px solid #e2e2e2;font-size:9.5px;color:#aaa;padding:8px 12px}
.sub-btn{position:absolute;left:155px;top:73px;width:82px;height:25px;border-radius:8px;background:linear-gradient(#fff,#d6d6d6);box-shadow:0 1px 3px rgba(0,0,0,.35);font-family:"Open Sans",sans-serif;font-size:11.5px;text-align:center;line-height:25px;color:#222}
.foot-nav{top:1133px;font-family:Georgia,serif;font-style:italic;font-weight:700;font-size:12px}
.foot-nav a{position:absolute;color:var(--red);text-decoration:none;white-space:nowrap}
.foot-nav a.current{color:#aaa}
.footer{left:0;top:1159px;width:1056px;height:41px;background:var(--dark);color:#9a9286;font-family:"Open Sans",sans-serif;font-size:9.5px}
.footer .copy{position:absolute;left:91px;top:14px}
.footer .follow{position:absolute;left:734px;top:17px}
.social{position:absolute;top:15px;width:13px;height:13px;border-radius:2px}
.footer .ver{position:absolute;left:903px;top:22px;font-size:8px}
</style>
</head>
<body>
<div class="abs header-band"></div>
<div class="abs brand">Vantra</div>
<nav class="abs main-nav">
  <a class="current" style="left:440px">Home</a>
  <a style="left:505px">About</a>
  <a style="left:570px">Jobs</a>
  <a style="left:626px">Blog</a>
  <a style="left:682px">Career</a>
  <a style="left:756px">Location</a>
  <a style="left:843px">Contact Us</a>
</nav>

<section class="abs hero"></section>
<div class="abs hero-photo" role="img" aria-label="Offshore oil rig silhouetted against a golden sunset"></div>
<div class="slide-dots"><span style="left:116px"></span><span style="left:135px"></span><span style="left:153px"></span><span class="on" style="left:172px"></span></div>
<h1 class="abs hero-title">JOB Search</h1>
<div class="abs hero-sub" style="top:154px">JOBS IN OIL &amp; GAS INDUSTRY</div>
<div class="abs hero-sub" style="top:178px">Apply Now For Middle East Jobs</div>
<p class="abs hero-note">Sed ut perspiciatis unde omnis iste natus error sit volupta-tem accusantium doloremque laudantium</p>
<div class="abs form-label" style="top:255px">Name</div>
<div class="abs form-label" style="top:293px">Location</div>
<div class="abs form-label" style="top:331px">Job</div>
<div class="abs field" style="top:253px"></div>
<div class="abs field" style="top:291px"></div>
<div class="abs field" style="top:329px"></div>
<div class="abs search-btn">SEARCH</div>
<svg class="abs slide-tab" viewBox="0 0 30 49"><path d="M30 0 A26 24.5 0 0 0 30 49 Z" fill="#b82503"/><path d="M19 17 L13 24.5 L19 32" stroke="#fff" stroke-width="3" fill="none"/></svg>
<div class="abs hero-shadow"></div>

<h2 class="abs welcome-title">Welcome To Our Website</h2>
<div class="abs welcome-photo" role="img" aria-label="Boat moored at a jetty at sunset"></div>
<div class="abs photo-shadow"></div>
<p class="abs body-copy copy-side">Lorem ipsum dolor sit amet, consectetur adipisicing elit, sed do eiusmod tempor incididunt ut labore et dolore magna aliqua. Ut enim ad minim veniam, quis nostrud exercitation ullamco laboris nisi ut <a>aliquip ex ea commodo consequat.</a> Duis aute irure dolor in reprehenderit in voluptate velit esse cillum dolore eu fugiat nulla pariatur. Excepteur sint occaecat cupidatat non proident, sunt in culpa qui officia deserunt mollit anim id est laborum. Lorem ipsum dolor sit amet, consectetur adipisicing elit, sed do eiusmod tempor i<a>ncididunt ut labore et dolore magna aliqua.</a> <a>Ut enim ad minim veniam, quis nostrud</a> exercitation ullamco</p>
<p class="abs body-copy copy-full">Lorem ipsum dolor sit amet, consectetur adipisicing elit, sed do eiusmod tempor incididunt ut labore et dolore magna aliqua. Ut enim ad minim veniam, quis nostrud exercitation ullamco laboris nisi ut <a>abore et dolore magna aliqua. Ut enim ad minim veniam, quis nostrud</a> exercitation ullamco laboris nisi ut aliquip ex ea commodo consequat. Duis aute irure dolor in reprehenderit in voluptate velit esse cillum mollit anim id est laborum.</p>

<aside class="abs box careers">
  <h2>Careers</h2>
  <ul>
    <li>Procedimentos</li>
    <li>Benefícios da Psicologia Online</li>
    <li>Cuidados antes do atendimento</li>
    <li>Sed ut perspiciatis unde omnis iste</li>
    <li>On the other hand,</li>
    <li>Nemo enim ipsam voluptatem</li>
    <li>Procedimentos</li>
    <li>Benefícios da Psicologia Online</li>
    <li>Cuidados antes do atendimento</li>
  </ul>
</aside>

<section class="abs box jobs">
  <h2 class="panel-title">Jobs</h2>
  <div class="job-item" style="top:52px">
    <div class="job-date">22-12-2012</div>
    <div class="job-head">Sed ut perspiciatis unde omnis</div>
    <div>explain to you how all this mistaken idea of denouncing pleasure .....</div>
    <a class="read-more">Read more</a>
  </div>
  <div class="job-item" style="top:164px">
    <div class="job-date">22-12-2012</div>
    <div class="job-head">Sed ut perspiciatis unde omnis</div>
    <div>explain to you how all this mistaken idea of denouncing pleasure .....</div>
    <a class="read-more">Read more</a>
  </div>
</section>

<section class="abs box testimonial">
  <h2 class="panel-title">Testimonial</h2>
  <span class="quote-mark" style="left:14px;top:34px">&#8220;</span>
  <p class="quote-text">Sed ut perspiciatis unde omnis iste natus error sit voluptatem accusantium doloremque laudantium, totam rem aperiam, eaque ipsa quae ab illo inventore veritatis et quasi architecto beatae vitae dicta sunt explicabo. <a>Nemo enim ipsam voluptatem quia</a> voluptas sit aspernatur aut odit aut fugit, sed quia consequuntur magni dolores eos qui ratione voluptatem sequi nesciunt.</p>
  <span class="quote-mark" style="left:238px;top:216px">&#8221;</span>
  <div class="quote-by">- Mara Dalen</div>
</section>

<section class="abs box call">
  <div class="abs call-photo" role="img" aria-label="Support agent wearing a headset"></div>
  <div class="call-title">Call us Now</div>
  <div class="call-phone">050 418 2270</div>
  <div class="call-btn">CLICK HERE
    <svg width="20" height="20" viewBox="0 0 20 20"><circle cx="10" cy="10" r="10" fill="#d42e05"/><path d="M8 6 L14 10 L8 14 Z" fill="#fff"/></svg>
  </div>
</section>

<section class="abs box newsletter">
  <h2>Newsletter</h2>
  <div class="mail-field">Enter your mail id</div>
  <div class="sub-btn">SUBSCRIBE</div>
</section>

<nav class="abs foot-nav">
  <a class="current" style="left:94px">Home</a>
  <a style="left:147px">About</a>
  <a style="left:200px">Jobs</a>
  <a style="left:245px">Blog</a>
  <a style="left:291px">Career</a>
  <a style="left:351px">Location</a>
  <a style="left:421px">Contact Us</a>
</nav>

<footer class="abs footer">
  <span class="copy">© 2012.www.vantra-jobs.com</span>
  <span class="follow">Follow us</span>
  <span class="social" style="left:783px;background:#e8761c"></span>
  <span class="social" style="left:801px;background:#3aa6d8"></span>
  <span class="social" style="left:819px;background:#3b5998"></span>
  <span class="social" style="left:837px;background:#555"></span>
  <span class="social" style="left:855px;background:#1f7ab8"></span>
  <span class="ver">M1</span>
</footer>
</body>
</html>
```